Webdesign für Holding-Firma
Zielgruppe
Die velunto Holding ist eine Holding-Firma mit drei Tochtergesellschaften: velunto trusted advisors, velutno Real estate und Velunto GmbH. Wir haben Beteiligungen in IT-Unternehmen, Real Estate sowie kleine und mittlere Startups.
Aufgabenstellung
Das Design sollte nicht zu bunt sein und eher schlicht und futuristisch gestaltet sein. Gerne können die Farben aus den verschiedenen Logos verarbeitet werden.

```html
<!DOCTYPE html>
<html lang="de">
<head>
<meta charset="utf-8">
<title>VELUNTO Holding</title>
<link href="https://fonts.googleapis.com/css2?family=Josefin+Sans:wght@400;600;700&display=swap" rel="stylesheet">
<style>
:root{
  --ink:#2b2b2d;
  --dark:#2e3138;
  --panel:#f3f3f3;
  --white:#ffffff;
  --muted:#8a8a8a;
}
*{box-sizing:border-box;margin:0;padding:0}
html,body{width:1200px;height:2359px;overflow:hidden;background:var(--white)}
body{position:relative;font-family:"Josefin Sans",sans-serif;color:var(--ink);letter-spacing:.06em}
.abs{position:absolute}
.hero{left:0;top:0;width:1200px;height:340px;background:linear-gradient(180deg,#c9ced3 0%,#e3e6ea 55%,#eef0f2 100%)}
.brand{left:137px;top:38px;display:flex;align-items:center;gap:8px;font-size:21px;font-weight:600;letter-spacing:.1em}
.brand-mark{width:20px;height:20px;border:2px solid var(--ink)}
.lang{right:125px;top:46px;font-size:11px;display:flex;gap:10px;align-items:center}
.burger{width:11px;height:8px;border-top:1px solid var(--ink);border-bottom:1px solid var(--ink);position:relative;margin-left:6px}
.burger::after{content:"";position:absolute;left:0;right:0;top:3px;border-top:1px solid var(--ink)}
.hero-title{left:0;width:1200px;top:202px;text-align:center;font-size:24px;font-weight:600;letter-spacing:.12em}
.scroll-down{left:590px;top:254px}
.sheet{left:0;width:1200px;background:var(--white);border-radius:60px 60px 0 0}
.panel{background:var(--panel)}
.heading{font-size:23px;font-weight:600;line-height:1.05;padding-left:12px;border-left:2px solid var(--ink)}
.intro{left:450px;top:414px;width:440px;font-size:11px;line-height:21px;letter-spacing:.05em}
.service{width:185px;height:130px}
.service .icon{position:absolute;left:0;top:0;width:82px;height:82px;background:var(--white);border-radius:8px;z-index:2;display:flex;align-items:center;justify-content:center}
.service .icon span{width:52px;height:52px;border-radius:6px;background:#e4e4e4}
.service .bar{position:absolute;left:0;top:70px;width:185px;height:60px;background:var(--dark);border-radius:8px;color:var(--white);font-size:10.5px;letter-spacing:.04em;display:flex;align-items:center;justify-content:center;padding:12px 10px 0;line-height:13px;white-space:nowrap}
.service .bar.left{justify-content:flex-start;padding-left:24px}
.holding{width:122px;height:190px}
.holding .logo{position:absolute;left:0;top:0;width:112px;height:78px;background:var(--white);border-radius:8px;z-index:2;display:flex;align-items:center;justify-content:center;font-size:12px;font-weight:600;color:#4a4a4a;letter-spacing:.02em}
.holding .body{position:absolute;left:0;top:54px;width:122px;height:136px;background:var(--dark);border-radius:8px;color:var(--white);padding:34px 0 0 9px}
.holding h3{font-size:13px;font-weight:600;letter-spacing:.05em;margin-bottom:8px}
.holding p{font-size:9px;line-height:10.5px;letter-spacing:.03em;margin-bottom:5px}
.holding svg{position:absolute;right:9px;bottom:8px}
.field{background:var(--white);border-radius:4px;font-size:11px;color:var(--muted);padding:13px 12px 0}
.send{left:158px;top:2087px;width:675px;height:33px;background:var(--dark);border-radius:17px;color:var(--white);font-size:9px;font-weight:700;letter-spacing:.12em;display:flex;align-items:center;justify-content:center;gap:14px}
.contact{left:877px;top:1926px;font-size:11px;line-height:15px}
.contact strong{font-weight:700}
.contact .row{display:flex;align-items:center;gap:8px;margin-bottom:5px}
.footer{left:0;top:2218px;width:1200px;height:141px;background:var(--dark);border-radius:48px 48px 0 0;color:#cfd2d6;font-size:10px;letter-spacing:0}
.footer .rule{position:absolute;left:158px;top:47px;width:926px;border-top:1px solid #8b8f95}
.footer .copy{position:absolute;left:161px;top:66px}
.footer .links{position:absolute;right:113px;top:64px;display:flex;gap:10px;align-items:center}
.social{width:11px;height:11px;border:1px solid #cfd2d6;border-radius:50%}
</style>
</head>
<body>

<div class="abs hero" role="img" aria-label="Unscharfes Foto von Geschäftsleuten in einer hellen Bürolobby"></div>
<div class="abs brand"><span class="brand-mark"></span>VELUNTO</div>
<div class="abs lang"><span>DE</span><span>|</span><span>EN</span><span class="burger"></span></div>
<h1 class="abs hero-title">VELUNTO HOLDING</h1>
<svg class="abs scroll-down" width="20" height="24" viewBox="0 0 20 24" fill="none" stroke="#2b2b2d" stroke-width="1"><circle cx="10" cy="14" r="8"/><path d="M10 0v18M6 14l4 4 4-4"/></svg>

<!-- about -->
<section class="abs sheet" style="top:310px;height:360px"></section>
<div class="abs panel" style="left:355px;top:315px;width:838px;height:250px;border-radius:0 60px 0 60px"></div>
<h2 class="abs heading" style="left:137px;top:407px">Wer sind<br>wir?</h2>
<p class="abs intro">Als das Unternehmen hinter der Marke VELUNTO group bieten wir führendes Branchenwissen, schlanke Lösungen und stabile Prozesse sowie Netzwerk für Unternehmen in allen Unternehmensphasen, vor allem in ITK Branche.</p>

<!-- services -->
<section class="abs sheet panel" style="top:663px;height:560px"></section>
<h2 class="abs heading" style="left:958px;top:763px">Was tun<br>wir?</h2>
<div class="abs service" style="left:137px;top:763px"><div class="icon" role="img" aria-label="Symbol Hände greifen ineinander"><span></span></div><div class="bar left">Wir bringen<br>Kompetenzen zusammen</div></div>
<div class="abs service" style="left:402px;top:763px"><div class="icon" role="img" aria-label="Symbol Zahnrad mit Personen"><span></span></div><div class="bar">Management Kompetenz</div></div>
<div class="abs service" style="left:667px;top:763px"><div class="icon" role="img" aria-label="Symbol Schachfiguren"><span></span></div><div class="bar">Holding Management</div></div>
<div class="abs service" style="left:137px;top:955px"><div class="icon" role="img" aria-label="Symbol Rechner und Stift"><span></span></div><div class="bar">Buchhaltung &amp; Controlling</div></div>
<div class="abs service" style="left:402px;top:955px"><div class="icon" role="img" aria-label="Symbol Lastwagen im Zahnrad"><span></span></div><div class="bar">Fuhrpark Management</div></div>
<div class="abs service" style="left:667px;top:955px"><div class="icon" role="img" aria-label="Symbol Megafon"><span></span></div><div class="bar">Marketing Excellence</div></div>

<!-- holdings -->
<section class="abs sheet" style="top:1183px;height:600px"></section>
<div class="abs panel" style="left:355px;top:1190px;width:845px;height:443px;border-radius:0 60px 0 60px"></div>
<h2 class="abs heading" style="left:137px;top:1281px;font-size:24px">Beteiligungen</h2>

<div class="abs holding" style="left:400px;top:1283px"><div class="logo">Voltnetz</div><div class="body"><h3>strombase</h3><p>Energiewirtschaftliche Softwarelösung</p><p>strombase GmbH<br>seit 2012</p><svg width="28" height="16" viewBox="0 0 28 16" fill="none" stroke="#fff"><circle cx="20" cy="8" r="7"/><path d="M0 8h24M21 5l3 3-3 3"/></svg></div></div>
<div class="abs holding" style="left:535px;top:1283px"><div class="logo">Feldmark</div><div class="body"><h3>strombase</h3><p>Energiewirtschaftliche Softwarelösung</p><p>strombase GmbH<br>seit 2012</p><svg width="28" height="16" viewBox="0 0 28 16" fill="none" stroke="#fff"><circle cx="20" cy="8" r="7"/><path d="M0 8h24M21 5l3 3-3 3"/></svg></div></div>
<div class="abs holding" style="left:670px;top:1283px"><div class="logo">Weitblick</div><div class="body"><h3>strombase</h3><p>Energiewirtschaftliche Softwarelösung</p><p>strombase GmbH<br>seit 2012</p><svg width="28" height="16" viewBox="0 0 28 16" fill="none" stroke="#fff"><circle cx="20" cy="8" r="7"/><path d="M0 8h24M21 5l3 3-3 3"/></svg></div></div>
<div class="abs holding" style="left:805px;top:1283px"><div class="logo">Tannhof</div><div class="body"><h3>strombase</h3><p>Energiewirtschaftliche Softwarelösung</p><p>strombase GmbH<br>seit 2012</p><svg width="28" height="16" viewBox="0 0 28 16" fill="none" stroke="#fff"><circle cx="20" cy="8" r="7"/><path d="M0 8h24M21 5l3 3-3 3"/></svg></div></div>
<div class="abs holding" style="left:940px;top:1283px"><div class="logo">Klarsicht</div><div class="body"><h3>strombase</h3><p>Energiewirtschaftliche Softwarelösung</p><p>strombase GmbH<br>seit 2012</p><svg width="28" height="16" viewBox="0 0 28 16" fill="none" stroke="#fff"><circle cx="20" cy="8" r="7"/><path d="M0 8h24M21 5l3 3-3 3"/></svg></div></div>

<div class="abs holding" style="left:400px;top:1490px"><div class="logo">Birkenau</div><div class="body"><h3>strombase</h3><p>Energiewirtschaftliche Softwarelösung</p><p>strombase GmbH<br>seit 2012</p><svg width="28" height="16" viewBox="0 0 28 16" fill="none" stroke="#fff"><circle cx="20" cy="8" r="7"/><path d="M0 8h24M21 5l3 3-3 3"/></svg></div></div>
<div class="abs holding" style="left:535px;top:1490px"><div class="logo">Quellwerk</div><div class="body"><h3>strombase</h3><p>Energiewirtschaftliche Softwarelösung</p><p>strombase GmbH<br>seit 2012</p><svg width="28" height="16" viewBox="0 0 28 16" fill="none" stroke="#fff"><circle cx="20" cy="8" r="7"/><path d="M0 8h24M21 5l3 3-3 3"/></svg></div></div>
<div class="abs holding" style="left:670px;top:1490px"><div class="logo">Lindgrün</div><div class="body"><h3>strombase</h3><p>Energiewirtschaftliche Softwarelösung</p><p>strombase GmbH<br>seit 2012</p><svg width="28" height="16" viewBox="0 0 28 16" fill="none" stroke="#fff"><circle cx="20" cy="8" r="7"/><path d="M0 8h24M21 5l3 3-3 3"/></svg></div></div>
<div class="abs holding" style="left:805px;top:1490px"><div class="logo">Kontorpost</div><div class="body"><h3>strombase</h3><p>Energiewirtschaftliche Softwarelösung</p><p>strombase GmbH<br>seit 2012</p><svg width="28" height="16" viewBox="0 0 28 16" fill="none" stroke="#fff"><circle cx="20" cy="8" r="7"/><path d="M0 8h24M21 5l3 3-3 3"/></svg></div></div>
<div class="abs holding" style="left:940px;top:1490px"><div class="logo">Kiesberg</div><div class="body"><h3>strombase</h3><p>Energiewirtschaftliche Softwarelösung</p><p>strombase GmbH<br>seit 2012</p><svg width="28" height="16" viewBox="0 0 28 16" fill="none" stroke="#fff"><circle cx="20" cy="8" r="7"/><path d="M0 8h24M21 5l3 3-3 3"/></svg></div></div>

<!-- contact -->
<section class="abs sheet panel" style="top:1780px;height:500px"></section>
<div class="abs field" style="left:158px;top:1880px;width:329px;height:38px">Name</div>
<div class="abs field" style="left:504px;top:1880px;width:329px;height:38px">E-Mail</div>
<div class="abs field" style="left:158px;top:1933px;width:675px;height:137px">Mitteilung</div>
<div class="abs send">ABSENDEN<svg width="20" height="6" viewBox="0 0 20 6" fill="none" stroke="#fff"><path d="M0 3h19M16 0l3 3-3 3"/></svg></div>
<h2 class="abs heading" style="left:865px;top:1875px;font-size:24px">Kontakt</h2>
<div class="abs contact">
  <p><strong>VELUNTO Holding GmbH</strong><br>Lindenallee 14<br>76532 Talheim</p>
  <div style="height:20px"></div>
  <div class="row"><svg width="15" height="11" viewBox="0 0 15 11" fill="none" stroke="#2b2b2d"><rect x=".5" y=".5" width="14" height="10"/><path d="M.5 .5l7 6 7-6"/></svg>kontakt@velunto-holding.de</div>
  <div class="row"><svg width="15" height="13" viewBox="0 0 15 13" fill="none" stroke="#2b2b2d"><path d="M3 1l3 3-2 2c1 2 2 3 4 4l2-2 3 3-2 2C6 12 1 7 1 3z"/></svg>+49 (7221) 480 215 60</div>
  <div class="row"><svg width="15" height="15" viewBox="0 0 15 15" fill="none" stroke="#2b2b2d"><path d="M7.5 14S2.5 9 2.5 5.5a5 5 0 0 1 10 0C12.5 9 7.5 14 7.5 14z"/><circle cx="7.5" cy="5.5" r="2"/></svg><span style="text-decoration:underline">Anfahrt &gt;</span></div>
  <div style="height:16px"></div>
  <p><strong>Rechtliches</strong><br>GF: Jonas Ferber und Lea Ferber<br>HRB 418260<br>Steuer-Nr.: 36102/47719</p>
</div>

<!-- footer -->
<footer class="abs footer">
  <div class="rule"></div>
  <p class="copy">© Copyright © 2020 VELUNTO Holding GmbH. Alle Rechte vorbehalten.</p>
  <div class="links"><span>Impressum</span><span>Datenschutz</span><span class="social" aria-label="Soziales Netzwerk"></span><span class="social" aria-label="Soziales Netzwerk"></span></div>
</footer>

</body>
</html>
```